Tolvern Business Cards

Business card design. dont mind if new logo is suggested.
it would be for a security company.
our clients would be bigger security companies around Australia.
have a logo done but can be replaced. see attaached. like the colors.
Need company name, person name, designation, phone and email on front.
At back company logo and name. website saddress and 2 x license numbers
would like to have 2 different background color for both sidde

Industry/Entity Type

Security

Contact Information for Business Card

round corners, front should be light in color. need logo at back with webaddress and 2 x license numners

Font styles to use
Sans Serif

Colors
f37122
faa54b
f8ba93
0255a3
0592cd
85cae6
b3d448
9bcb3c
ffffff

Requirements
Must have
• see description
Nice to have
• see description
Should not have
• should not be difficult to read or hardd to find information on card.. lets say easy on eyes yet catchy

```html
<!DOCTYPE html>
<html lang="en">
<head>
<meta charset="utf-8">
<title>Tolvern Security Group – Business Cards</title>
<link rel="stylesheet" href="https://fonts.googleapis.com/css2?family=Crimson+Text:wght@600&family=Roboto:wght@400;500&family=Roboto+Condensed:wght@700&display=swap">
<style>
  :root {
    --backdrop: #2e2f31;
    --paper: #f2f2f2;
    --navy: #0d2f63;
    --navy-deep: #0e2d58;
    --teal: #0aa3cb;
    --teal-soft: #1fa9d0;
    --ink-grey: #4d4d4d;
    --white: #ffffff;
  }
  * { margin: 0; padding: 0; box-sizing: border-box; }
  html, body { width: 1200px; height: 960px; overflow: hidden; }
  body {
    background: var(--backdrop);
    position: relative;
    font-family: "Roboto", Arial, sans-serif;
  }
  .card {
    position: absolute;
    width: 600px;
    height: 342px;
    border-radius: 3px;
    overflow: hidden;
  }

  /* Front */
  .card--front { left: 314px; top: 113px; background: var(--paper); }
  .brand {
    position: absolute;
    right: 36px;
    top: 34px;
    display: flex;
    flex-direction: column;
    align-items: center;
    gap: 14px;
  }
  .brand__dot {
    width: 78px; height: 78px; border-radius: 50%;
    background: var(--teal);
  }
  .brand__name {
    font-family: "Crimson Text", Georgia, serif;
    font-weight: 600;
    font-size: 19px;
    letter-spacing: 0.2px;
    color: var(--navy);
    white-space: nowrap;
  }
  .person { position: absolute; left: 37px; top: 195px; }
  .person__name {
    font-family: "Roboto Condensed", "Arial Narrow", sans-serif;
    font-weight: 700;
    font-size: 23px;
    color: var(--navy);
    line-height: 1;
  }
  .person__role {
    margin-top: 7px;
    font-weight: 500;
    font-size: 15px;
    color: var(--teal);
    line-height: 1;
  }
  .divider {
    position: absolute; left: 37px; right: 37px; top: 245px;
    height: 1px; background: var(--teal);
  }
  .contact {
    position: absolute; left: 37px; top: 255px;
    list-style: none;
    font-size: 14px; color: var(--ink-grey); line-height: 19px;
  }
  .contact__item { display: flex; align-items: center; gap: 8px; }
  .contact__icon { width: 13px; height: 13px; fill: var(--navy); }
  .address {
    position: absolute; right: 38px; top: 255px;
    font-style: normal; text-align: right;
    font-size: 14px; color: var(--ink-grey); line-height: 19px;
  }
  .footer-bands { position: absolute; left: 0; bottom: 0; width: 600px; height: 32px; }
  .footer-web {
    position: absolute; right: 35px; bottom: 9px;
    font-size: 14px; letter-spacing: 2.6px; color: var(--white);
  }

  /* Back */
  .card--back { left: 311px; top: 472px; background: var(--navy-deep); }
  .back-mark {
    position: absolute; left: 16px; top: 22px;
    width: 310px; height: 310px; border-radius: 50%;
    background: var(--teal-soft);
    opacity: 0.85;
  }
  .back-info { position: absolute; right: 20px; top: 258px; text-align: center; }
  .back-info__name {
    font-family: "Crimson Text", Georgia, serif;
    font-weight: 600; font-size: 20px; color: var(--white);
    line-height: 1; white-space: nowrap;
  }
  .back-info__web {
    margin-top: 4px; font-size: 15px; letter-spacing: 3.4px;
    color: var(--teal); line-height: 1.2;
  }
  .back-info__licence {
    margin-top: 4px; font-size: 14px; color: var(--white); line-height: 1.3;
  }
</style>
</head>
<body>

<section class="card card--front" aria-label="Business card front">
  <div class="brand">
    <span class="brand__dot"></span>
    <span class="brand__name">TOLVERN SECURITY GROUP</span>
  </div>

  <div class="person">
    <p class="person__name">DANIEL REEVE</p>
    <p class="person__role">CEO/FOUNDER</p>
  </div>
  <div class="divider"></div>

  <ul class="contact">
    <li class="contact__item">
      <svg class="contact__icon" viewBox="0 0 24 24" aria-hidden="true"><path d="M6.6 10.8a15.1 15.1 0 0 0 6.6 6.6l2.2-2.2c.3-.3.7-.4 1-.2 1.1.4 2.3.6 3.6.6.6 0 1 .4 1 1V20c0 .6-.4 1-1 1A17 17 0 0 1 3 4c0-.6.4-1 1-1h3.5c.6 0 1 .4 1 1 0 1.3.2 2.5.6 3.6.1.3 0 .7-.2 1z"/></svg>
      612 555 0148
    </li>
    <li class="contact__item">
      <svg class="contact__icon" viewBox="0 0 24 24" aria-hidden="true"><path d="M2 5h20v14H2z" fill="none"/><path d="M2 5h20v2l-10 6L2 7zM2 9l10 6 10-6v10H2z"/></svg>
      info@tolvern.com
    </li>
  </ul>

  <address class="address">418 Wattle Crescent<br>Brisbane, Queensland 4000</address>

  <svg class="footer-bands" viewBox="0 0 600 32" aria-hidden="true">
    <rect x="0" y="20" width="600" height="12" fill="var(--navy)"/>
    <path d="M0 8 H334 Q338 8 336 18 L334 20 H0 Z" fill="var(--teal)"/>
    <path d="M322 20 Q336 20 340 10 Q344 0 356 0 H600 V32 H322 Z" fill="var(--navy)"/>
    <path d="M0 20.5 H324 Q338 20 342 10 Q346 1 356 1" fill="none" stroke="var(--white)" stroke-width="1.2"/>
  </svg>
  <span class="footer-web">www.tolvern.com</span>
</section>

<section class="card card--back" aria-label="Business card back">
  <div class="back-mark"></div>
  <div class="back-info">
    <p class="back-info__name">TOLVERN SECURITY GROUP</p>
    <p class="back-info__web">www.tolvern.com</p>
    <p class="back-info__licence">Lic No. #40917326 &nbsp;|&nbsp; #73051849</p>
  </div>
</section>

</body>
</html>
```